Dental Office Needs- Flyer Design for Same Day Crowns

We need a flyer that will explain the benefits of the same day crown from the patient prospective. Not show pictures of the machine that makes the crowns. See attached material for content. The flyer should use the practices PMS colors of Green 562 and Blue 3025. The ad should say to the patient - I want to go this office and get my crown done there.
Updates

Project Deadline Extended Reason: The difference in the time zone between USA and Europe has caused issues. Minor changes still need to be worked out. Added Thursday, July 14, 2016

Target Market(s)

Dental Patients

Industry/Entity Type

Dental

Requirements
Must have
• Call to Action
• Business Address and Business Logo
• Classic Design
• images of a Happy 50 year old Couple
• Gives the benefits of the same day crown
Should not have
• No Images of tooth figures
• No before or after pictures

```html
<!DOCTYPE html>
<html lang="en">
<head>
<meta charset="utf-8">
<title>Ashgrove Dental Care – Same-Day Crowns</title>
<link href="https://fonts.googleapis.com/css2?family=Roboto+Condensed:wght@400;700;900&family=Cormorant+Garamond:wght@500&display=swap" rel="stylesheet">
<style>
  :root {
    --blue: #0d4b72;
    --green: #0b7566;
    --ink: #1c1c1c;
    --white: #ffffff;
    --rule: #6b6b6b;
  }
  * { box-sizing: border-box; margin: 0; padding: 0; }
  html, body { width: 1012px; height: 1200px; overflow: hidden; background: #e4e7e9; }
  .flyer {
    position: relative; width: 1012px; height: 1200px; overflow: hidden;
    background: var(--white); font-family: "Roboto Condensed", Arial, sans-serif; color: var(--ink);
  }
  .hero-photo {
    position: absolute; left: 0; top: 200px; width: 1012px; height: 330px; z-index: 1;
    background: linear-gradient(100deg, #3f5a22 0%, #7c9a3e 30%, #c7d2b8 52%, #4f6f9a 72%, #2f4f7c 100%);
  }
  .header-shapes { position: absolute; left: 0; top: 0; width: 1012px; height: 210px; z-index: 2; }
  .brand {
    position: absolute; left: 40px; top: 92px; z-index: 3;
    display: flex; align-items: center; gap: 10px;
    font-family: "Cormorant Garamond", Georgia, serif; font-weight: 500;
    font-size: 32px; color: var(--blue);
  }
  .brand-dot { width: 16px; height: 16px; border-radius: 50%; background: var(--green); }
  .headline {
    position: absolute; right: 48px; top: 24px; z-index: 3;
    text-align: right; color: var(--white);
    font-weight: 900; font-size: 38px; line-height: 40px; text-transform: uppercase;
  }
  .goodbye-band { position: absolute; left: 0; top: 515px; width: 500px; height: 110px; z-index: 2; }
  .goodbye-list {
    position: absolute; left: 48px; top: 526px; z-index: 3; list-style: none;
    color: var(--white); font-weight: 700; font-size: 21px; line-height: 30px; text-transform: uppercase;
  }
  .benefit-points {
    position: absolute; left: 52px; top: 640px; width: 520px; list-style: none;
    font-size: 19px; line-height: 24px;
  }
  .benefit-points li { position: relative; padding-left: 18px; margin-bottom: 8px; }
  .benefit-points li::before {
    content: ""; position: absolute; left: 2px; top: 9px; width: 7px; height: 7px; border-radius: 50%; background: var(--ink);
  }
  .digital-column {
    position: absolute; left: 600px; top: 545px; width: 370px; height: 265px;
    border-left: 2px solid var(--ink); padding-left: 20px;
  }
  .digital-intro { color: var(--green); font-weight: 700; font-size: 19px; line-height: 24px; margin-bottom: 8px; }
  .digital-list { list-style: none; font-size: 18px; width: 330px; }
  .digital-list li { padding: 6px 0 5px; border-bottom: 1px solid var(--rule); }
  .digital-list li:last-child { border-bottom: none; }
  .restoration-photos { display: flex; gap: 6px; margin-top: 6px; }
  .restoration-photos span { width: 112px; height: 50px; }
  .restoration-photos .metal { background: linear-gradient(90deg, #6b4b45, #9a8d86, #d9c9b5); }
  .restoration-photos .ceramic { background: linear-gradient(90deg, #b5553b, #e7b49a, #c86a4c); }
  .restorations-panel { position: absolute; left: 0; top: 820px; width: 1012px; height: 380px; }
  .restorations-copy { position: absolute; left: 64px; top: 870px; width: 890px; color: var(--white); }
  .restorations-title { font-weight: 900; font-size: 38px; line-height: 44px; text-transform: uppercase; margin-bottom: 8px; }
  .restorations-lead { font-size: 19px; line-height: 24px; margin-bottom: 14px; }
  .restorations-body { font-size: 18px; line-height: 23px; }
  .contact-band { position: absolute; left: 0; top: 1090px; width: 640px; height: 110px; }
  .contact { position: absolute; left: 64px; top: 1098px; color: var(--white); }
  .phone { display: flex; align-items: center; gap: 16px; font-weight: 900; font-size: 48px; line-height: 56px; letter-spacing: 2px; }
  .address { display: flex; align-items: center; gap: 6px; font-size: 18px; margin-top: 6px; }
</style>
</head>
<body>
<main class="flyer">
  <div class="hero-photo" role="img" aria-label="Photo of a smiling older couple sitting close together outdoors in a sunny garden"></div>

  <svg class="header-shapes" viewBox="0 0 1012 210" aria-hidden="true">
    <polygon points="0,0 1012,0 1012,190 500,205 0,205" fill="var(--white)"/>
    <polygon points="330,0 380,0 500,205 450,205" fill="var(--green)"/>
    <polygon points="370,0 1012,0 1012,190 500,205" fill="var(--blue)"/>
  </svg>
  <div class="brand"><span class="brand-dot"></span>Ashgrove Dental Care</div>
  <h1 class="headline">Are you ready for a<br>dramatically improved<br>experience with<br>your next crown?</h1>

  <svg class="goodbye-band" viewBox="0 0 500 110" aria-hidden="true">
    <polygon points="0,0 420,0 500,110 0,110" fill="var(--green)"/>
  </svg>
  <ul class="goodbye-list">
    <li>Good-bye temporary crown</li>
    <li>Good-bye second appointment</li>
    <li>Good-bye gooey messy impressions</li>
  </ul>

  <ul class="benefit-points">
    <li>Ashgrove Dental Care is pleased to offer you the Comfort and Convenience of One Visit Dental Care.</li>
    <li>We understand how hard it can be to take off work or have someone take care of the kids even once, but twice?</li>
    <li>Now with 3D CADCAM Technology, we can digitally design and mill a Customized, Ceramic Restoration in one appointment.</li>
  </ul>

  <aside class="digital-column">
    <p class="digital-intro">When it comes to your next<br>crown, the benefits of a Digital<br>Restoration add up quickly!</p>
    <ul class="digital-list">
      <li>A Same-Day Restoration</li>
      <li>A Stronger More Precise Fit</li>
      <li>A Beautiful Natural Appearance</li>
    </ul>
    <div class="restoration-photos">
      <span class="metal" role="img" aria-label="Close-up photo of teeth with a metal filling"></span>
      <span class="ceramic" role="img" aria-label="Close-up photo of teeth with a ceramic restoration"></span>
    </div>
  </aside>

  <svg class="restorations-panel" viewBox="0 0 1012 380" aria-hidden="true">
    <polygon points="0,40 610,40 630,0 1012,0 1012,380 0,380" fill="var(--blue)"/>
  </svg>
  <section class="restorations-copy">
    <h2 class="restorations-title">Same-Day Digital Restorations.</h2>
    <p class="restorations-lead">Crowns, veneers and bridges that happen in hours instead of days.<br>Ask your dentist if digital dentistry is right for you.</p>
    <p class="restorations-body">Restorative dentistry has evolved and now, digital technology allows us to take an impression of your teeth with a digital scanner and create your restoration right in our office. We can match your existing teeth and provide you with a filling, veneer, crown or bridge using the most advanced non-metal composite materials giving you a beautiful smile and natural appearance.</p>
  </section>

  <svg class="contact-band" viewBox="0 0 640 110" aria-hidden="true">
    <polygon points="0,0 600,0 640,22 600,44 600,110 0,110" fill="var(--green)"/>
  </svg>
  <div class="contact">
    <div class="phone">
      <svg width="38" height="38" viewBox="0 0 40 40" aria-hidden="true">
        <rect width="40" height="40" rx="7" fill="var(--white)"/>
        <path d="M13 9c2 0 3 4 4 6 0 2-3 2-2 4 2 3 3 4 6 6 2 1 2-2 4-2 2 1 6 2 6 4s-3 5-6 4C17 29 11 23 9 15c-1-3 2-6 4-6z" fill="var(--green)"/>
      </svg>
      0000 000 0000
    </div>
    <div class="address">
      <svg width="16" height="20" viewBox="0 0 16 20" aria-hidden="true">
        <path d="M8 0a7 7 0 0 0-7 7c0 5 7 13 7 13s7-8 7-13a7 7 0 0 0-7-7zm0 10a3 3 0 1 1 0-6 3 3 0 0 1 0 6z" fill="var(--white)"/>
      </svg>
      : XXXXXX XXXXXXX XXXXXXX XXXXXXX XXXXXX XXXX
    </div>
  </div>
</main>
</body>
</html>
```